Retirement Plan Advisor Bio

See the attached document and photo for content. I would like someone to design this one page flyer using my logo. This logo was designed by a designer with sketch hive. I am looking for a professional looking document. I want to he color scheme to be primarily white and gold.

Target Market(s)

Employers who offer a retirement plan

Requirements
Should not have
• The designs that I have received look more like resumes. I am interested in advertising my Retirement plan services. If anyone can change their submissions and change it to an ad for retirement plan services instead of a Bio or resume, I would prefer that.

```html
<!DOCTYPE html>
<html lang="en">
<head>
<meta charset="utf-8">
<title>Retirement Plan Advisor</title>
<link href="https://fonts.googleapis.com/css2?family=Montserrat:wght@400;500;600;700&display=swap" rel="stylesheet">
<style>
  :root {
    --gold: #a68a45;
    --gold-box: #a3863f;
    --ink: #111111;
    --paper: #ffffff;
    --light: #ffffff;
  }
  * { margin: 0; padding: 0; box-sizing: border-box; }
  html, body { width: 846px; height: 1200px; overflow: hidden; background: var(--paper); }
  body { font-family: "Montserrat", sans-serif; color: var(--ink); }
  .flyer { position: relative; width: 846px; height: 1200px; overflow: hidden; }

  .portrait {
    position: absolute; inset: 0;
    background:
      radial-gradient(ellipse 260px 300px at 230px 420px, #e6b39f 0%, #d9a48f 45%, rgba(217,164,143,0) 100%),
      radial-gradient(ellipse 320px 260px at 120px 60px, #d8c08f 0%, rgba(216,192,143,0) 100%),
      radial-gradient(ellipse 300px 260px at 800px 1150px, #161819 0%, #1e2123 50%, rgba(30,33,35,0) 100%),
      linear-gradient(135deg, #cfb487 0%, #d7a793 30%, #7d8aa3 62%, #566684 100%);
  }

  .intro-card {
    position: absolute; left: 423px; top: 92px; width: 374px; height: 646px;
    background: var(--paper); padding: 52px 0 0 51px;
  }
  .brand { display: flex; align-items: center; gap: 10px; height: 62px; }
  .brand-mark { width: 14px; height: 14px; background: var(--gold); }
  .brand-name { color: var(--gold); font-weight: 500; font-size: 20px; letter-spacing: 0.3px; }
  .advisor-name { margin-top: 22px; color: var(--gold); font-weight: 700; font-size: 25px; line-height: 30px; }
  .credentials { color: var(--ink); font-weight: 700; font-size: 25px; line-height: 32px; }
  .headline {
    margin-top: 18px; color: var(--gold); font-weight: 600;
    font-size: 41px; line-height: 45px; letter-spacing: -0.2px;
  }
  .mission { margin-top: 24px; width: 270px; font-size: 16.3px; line-height: 22.2px; font-weight: 500; }
  .mission strong { font-weight: 700; text-decoration: underline; text-underline-offset: 3px; }

  .details-panel {
    position: absolute; left: 0; top: 790px; width: 524px; height: 410px;
    background: var(--paper); padding: 30px 0 0 72px;
  }
  .section-title { font-weight: 500; font-size: 20px; line-height: 26px; }
  .bullet-list { list-style: none; margin-top: 7px; }
  .bullet-list li {
    position: relative; padding-left: 31px; font-size: 13.4px; line-height: 15.8px;
    margin-bottom: 8px; width: 350px;
  }
  .bullet-list li::before {
    content: ""; position: absolute; left: 13px; top: 5px; width: 6px; height: 6px;
    border-radius: 50%; background: var(--gold);
  }
  .qualifications { margin-top: 12px; }
  .qualifications .bullet-list li { margin-bottom: 4.5px; }

  .education-box {
    position: absolute; left: 476px; top: 868px; width: 321px; height: 188px;
    background: var(--gold-box); color: var(--light); padding: 26px 20px 0 35px;
  }
  .education-box h2 { font-weight: 600; font-size: 20px; line-height: 26px; }
  .degree { margin-top: 14px; font-size: 13.4px; }
  .disclosure { margin-top: 14px; font-size: 9.6px; line-height: 12px; }

  .contact {
    position: absolute; left: 567px; top: 1086px; color: var(--light);
    font-weight: 500; font-size: 12.6px; line-height: 14.6px;
  }
</style>
</head>
<body>
<div class="flyer">
  <div class="portrait" role="img" aria-label="Portrait photograph of the advisor smiling, against a blue-grey studio backdrop"></div>

  <section class="intro-card">
    <div class="brand">
      <span class="brand-mark"></span>
      <span class="brand-name">Verity Wealth, LLC</span>
    </div>
    <h1 class="advisor-name">Clara J Whitmore</h1>
    <p class="credentials">CFP® AIF®</p>
    <p class="headline">Qualified<br>Professional<br>Retirement<br>Plan Advisor</p>
    <p class="mission">I strive <strong>to improve retirement outcomes</strong> for my plan sponsor clients and their employees through careful retirement plan design assistance, strategic and targeted communication and education, as well as <strong>continual monitoring of results.</strong></p>
  </section>

  <section class="details-panel">
    <h2 class="section-title">Professional Specialties</h2>
    <ul class="bullet-list">
      <li>Over 18 years of experience in the retirement plan industry.</li>
      <li>Focused on helping plan sponsors reduce administrative burdens and fiduciary risk.</li>
      <li>Dedicated to helping employees work toward a positive retirement outcome through careful analysis of their savings rate, investment strategy and overall financial wellness..</li>
    </ul>
    <div class="qualifications">
      <h2 class="section-title">Qualifications</h2>
      <ul class="bullet-list">
        <li>Certified Financial Planner®</li>
        <li>Accredited Investment Fiduciary®</li>
        <li>Investment Advisor Representative</li>
        <li>Series 7, 63, and 65 Securities licenses with Keystone Securities</li>
        <li>Holds Life and Health Insurance licenses from Illinois</li>
      </ul>
    </div>
  </section>

  <aside class="education-box">
    <h2>Education</h2>
    <p class="degree">BS Brookhaven University, 1987</p>
    <p class="disclosure">*Securities and Investment Advisory Services offered through Keystone Securities Group, Inc., a Registered Broker/Dealer and Investment Advisor, member NSRB/IPSC</p>
  </aside>

  <address class="contact" style="font-style:normal">
    2400 Larkmoor Ave.<br>
    Fairview, IL 60400<br>
    (555) 014 2290<br>
    clara.whitmore@keystonesec.com<br>
    www.clarawhitmore.com
  </address>
</div>
</body>
</html>
```